Quorvex - Automated robotic Inspection with AI need new business cards

We need a new design of our business cards. The company is focused on automated quality control at high speed with unmatched results. We have a logo but need a more forward leaning business card that shows that we are delivering cutting edge technology.

Contact Information for Business Card

Name
Position
Adress
Phone
Email
e.g.
Lena Holmqvist
Chief Financial Officer (CFO)

Quorvex Sweden AB
Bruksvägen 14, SE-175 43 JÄRFÄLLA, Sweden
Mobile: +46735 21 47 83 | Office: +46 8 61 94 27
www.quorvex-example.com

Font styles to use
Sans Serif

```html
<!DOCTYPE html>
<html lang="en">
<head>
<meta charset="UTF-8">
<title>Quorvex – Business Card</title>
<link rel="stylesheet" href="https://fonts.googleapis.com/css2?family=Exo+2:wght@400;700&display=swap">
<style>
  :root {
    --backdrop: #262626;
    --brand-blue: #1b5a8c;
    --brand-blue-deep: #164c78;
    --ink: #2e2e2e;
    --rule: #9a9a9a;
    --card-top: #ffffff;
    --card-bottom: #e6e6e6;
    --white: #ffffff;
  }
  * { margin: 0; padding: 0; box-sizing: border-box; }
  html, body {
    width: 1200px; height: 1108px; overflow: hidden;
    background: var(--backdrop);
    font-family: "Exo 2", sans-serif;
  }
  .stage {
    width: 1200px; height: 1108px;
    display: flex; align-items: center; justify-content: center; gap: 80px;
  }
  .card {
    width: 400px; height: 620px; border-radius: 22px; position: relative; overflow: hidden;
  }
  .card--front {
    background: linear-gradient(180deg, var(--card-top) 0%, var(--card-bottom) 100%);
    color: var(--ink); text-align: center; padding: 96px 36px 0;
  }
  .brand-name {
    font-size: 64px; font-weight: 700; color: var(--brand-blue);
    letter-spacing: 2px; line-height: 1;
  }
  .person { margin-top: 118px; }
  .person__name {
    font-size: 27px; font-weight: 700; color: var(--brand-blue);
    text-transform: uppercase; letter-spacing: 0.5px; line-height: 1.1;
  }
  .person__title { font-size: 19px; margin-top: 4px; }
  .icon-row {
    display: flex; align-items: center; gap: 6px; margin-top: 18px;
  }
  .icon-row__rule { flex: 1; height: 1px; background: var(--rule); }
  .icon {
    width: 34px; height: 34px; border-radius: 7px; background: var(--brand-blue);
    display: flex; align-items: center; justify-content: center;
  }
  .icon svg { width: 22px; height: 22px; }
  .contact { margin-top: 14px; font-size: 19px; line-height: 27px; }
  .contact .accent { color: var(--brand-blue); }
  .divider { height: 1px; background: var(--rule); margin: 14px 34px 0; }
  .company { margin-top: 14px; font-size: 19px; line-height: 25px; }
  .company__name { font-weight: 700; color: var(--brand-blue); text-transform: uppercase; }
  .address__city { text-transform: uppercase; }

  .card--back { background: var(--brand-blue); }
  .back-texture {
    position: absolute; inset: 0;
    background: linear-gradient(160deg, var(--brand-blue) 0%, var(--brand-blue-deep) 100%);
  }
  .back-brand {
    position: absolute; left: 0; right: 0; top: 470px; text-align: center;
    font-size: 26px; font-weight: 700; color: var(--white); letter-spacing: 1px;
  }
</style>
</head>
<body>
<main class="stage">
  <section class="card card--front" aria-label="Business card front">
    <div class="brand-name">Quorvex</div>

    <div class="person">
      <div class="person__name">Lena Holmqvist</div>
      <div class="person__title">Chief Financial Officer (CFO)</div>
    </div>

    <div class="icon-row">
      <span class="icon-row__rule"></span>
      <span class="icon" aria-label="Phone">
        <svg viewBox="0 0 24 24" fill="none" stroke="#fff" stroke-width="1.8" stroke-linejoin="round">
          <path d="M4 9c0-3 3-4 8-4s8 1 8 4l-3 1-1-2H8L7 10z"/>
          <rect x="7" y="11" width="10" height="8" rx="1.5"/>
        </svg>
      </span>
      <span class="icon" aria-label="Mobile">
        <svg viewBox="0 0 24 24" fill="none" stroke="#fff" stroke-width="1.8">
          <rect x="7" y="3" width="10" height="18" rx="2"/>
          <line x1="11" y1="18" x2="13" y2="18"/>
        </svg>
      </span>
      <span class="icon" aria-label="Email">
        <svg viewBox="0 0 24 24" fill="none" stroke="#fff" stroke-width="1.8" stroke-linejoin="round">
          <rect x="3" y="6" width="18" height="12" rx="1"/>
          <path d="M3 6l9 7 9-7"/>
        </svg>
      </span>
      <span class="icon" aria-label="Website">
        <svg viewBox="0 0 24 24" fill="none" stroke="#fff" stroke-width="1.8">
          <circle cx="12" cy="12" r="8.5"/>
          <ellipse cx="12" cy="12" rx="3.5" ry="8.5"/>
          <line x1="3.5" y1="12" x2="20.5" y2="12"/>
        </svg>
      </span>
      <span class="icon-row__rule"></span>
    </div>

    <div class="contact">
      <div>+46 8 61 94 27</div>
      <div>+46735 21 47 83</div>
      <div>info@quorvex-example.com</div>
      <div>www.<span class="accent">quorvex-example</span>.com</div>
    </div>

    <div class="divider"></div>

    <div class="company">
      <div class="company__name">Quorvex Sweden AB</div>
      <div>Bruksvägen 14, SE-175 43</div>
      <div><span class="address__city">Järfälla</span>, Sweden</div>
    </div>
  </section>

  <section class="card card--back" aria-label="Business card back">
    <div class="back-texture" role="img" aria-label="Tone-on-tone blue repeating brand pattern"></div>
    <div class="back-brand">Quorvex</div>
  </section>
</main>
</body>
</html>
```